Cover needed for Sonqueue/plavio/digital release

Cover design needed for a Reggae song to be released as a single on sonqueue/ disc nest/ plavio/ vidarama etc... for the artist it should say Marcus Velden Meets Bluvaros and the song: Step and Sway Out. At the top it should say Marcus Velden and (Meets Bluvaros) can be in smaller letters. and the song title towards the bottom. Plus I would also like the same cover done without (Meets Bluvaros) included in the picture. So in total 2 images. The image theme can be reggae/ dancehall/ rub a dub/ vinyl turntable related. Here is some information about the image quality that the website I am using wants it in:
1400 x 1400 pixels minimum; 3000 x 3000 pixels maximum
PNG, GIF, JPG, or JPEG file type
72 - 300dpi (300dpi is the best)
Less than 25mb
RGB color scheme (not CMYK)
Unique to this particular title. We cannot accept artwork that has been used for another title.
Uploaded image must match your physical album cover artwork.
IMPORTANT: If your artist name and the title of your album or single appear on your cover artwork, it MUST precisely match the information you provided for this project. The text should be identical. For instance, if the artist name you provided is "Perry & Lindqvist (featuring Moss & Tarrant)," the text on your artwork should NOT say "Perry and Lindqvist."
Updates
I upgraded to be able to choose from more designs. Thank You
Target Market(s)
target market: Just Reggae fans dub fans, rub a dub/dancehall fans,

```html
<!DOCTYPE html>
<html lang="en">
<head>
<meta charset="utf-8">
<title>Marcus Velden – Step and Sway Out</title>
<link rel="stylesheet" href="https://fonts.googleapis.com/css2?family=Titan+One&family=Passion+One:wght@700&display=swap">
<style>
  :root {
    --wall-yellow: #cdc11b;
    --wall-olive: #9faa2c;
    --wall-green: #1d7d55;
    --deep-green: #167452;
    --shadow-red: #a50c10;
    --artist-red: #960d10;
    --title-white: #ffffff;
  }
  html, body {
    margin: 0;
    padding: 0;
    width: 1200px;
    height: 1200px;
    overflow: hidden;
    background: var(--wall-green);
  }
  .cover {
    position: relative;
    width: 1200px;
    height: 1200px;
    overflow: hidden;
    background: linear-gradient(162deg,
      var(--wall-yellow) 0%,
      var(--wall-yellow) 44%,
      var(--wall-olive) 58%,
      var(--wall-green) 74%,
      var(--deep-green) 100%);
  }
  .cover-art {
    position: absolute;
    inset: 0;
    width: 1200px;
    height: 1200px;
  }
  .long-shadow { fill: var(--shadow-red); }
  .wall-grain { mix-blend-mode: multiply; opacity: 0.35; }
  .artist-name {
    font-family: "Passion One", "Titan One", sans-serif;
    font-weight: 700;
    font-size: 66px;
    fill: var(--artist-red);
    letter-spacing: 1px;
  }
  .title-line {
    font-family: "Titan One", sans-serif;
    fill: var(--title-white);
  }
  .title-big { font-size: 232px; }
  .title-small { font-size: 112px; }
  .title-mid { font-size: 158px; }
</style>
</head>
<body>
<main class="cover">
  <svg class="cover-art" viewBox="0 0 1200 1200" xmlns="http://www.w3.org/2000/svg" aria-label="Marcus Velden – Step and Sway Out">
    <defs>
      <filter id="grain" x="0" y="0" width="100%" height="100%">
        <feTurbulence type="fractalNoise" baseFrequency="0.9" numOctaves="2" seed="7"/>
        <feColorMatrix type="matrix" values="0 0 0 0 0.2  0 0 0 0 0.2  0 0 0 0 0.1  0 0 0 -2.2 1.35"/>
      </filter>
    </defs>

    <polygon class="long-shadow"
      points="0,620 184,436 1032,436 1040,604 960,684 1080,708 1084,828 712,1200 0,1200"/>

    <rect class="wall-grain" x="0" y="0" width="1200" height="1200" filter="url(#grain)"/>

    <text class="artist-name" x="600" y="118" text-anchor="middle">MARCUS VELDEN</text>

    <text class="title-line title-big" x="612" y="606" text-anchor="middle" textLength="850" lengthAdjust="spacingAndGlyphs">STEP</text>
    <text class="title-line title-small" x="614" y="694" text-anchor="middle">and</text>
    <text class="title-line title-mid" x="614" y="826" text-anchor="middle" textLength="940" lengthAdjust="spacingAndGlyphs">SWAY OUT</text>
  </svg>
</main>
</body>
</html>
```